mental health business card

Double sided business card with logo on front and practitioners details on back.
The front of card should be while and back either blue or grey to match logo.

Space on back for appointment date and time to be written.

Please note that details are not available yet for address etc as currently moving 4500km across Australia. Just use generic or old info from attached letterhead.
Updates

Dear Designers,

Please note business card is also appointment card must have area where  date and time of clients next appointment can be written in.

Target Market(s)

This is card for patients and colleagues

Industry/Entity Type

Mental Health

Requirements
Must have
• Name
Director / Clinical Psychologist
email
web
phone
phone

Nice to have
• embossing on front of card

```html
<!DOCTYPE html>
<html lang="en">
<head>
<meta charset="utf-8">
<title>Clearview Wellbeing – Stationery</title>
<link href="https://fonts.googleapis.com/css2?family=Marcellus&family=EB+Garamond:ital,wght@1,500;1,700&display=swap" rel="stylesheet">
<style>
  :root {
    --backdrop: #2b2b2d;
    --paper: #ffffff;
    --cyan: #1ba9cf;
    --teal: #0f6f96;
    --navy: #14285a;
    --ink: #3a4868;
    --mark-grey: #7d7f88;
    --label: #0e1b3c;
    --value: #8d9bb8;
    --rule: #b7bfcf;
  }
  * { margin: 0; padding: 0; box-sizing: border-box; }
  html, body { width: 1200px; height: 1200px; overflow: hidden; }
  body { background: var(--backdrop); position: relative; font-family: "Marcellus", serif; }

  .card { position: absolute; overflow: hidden; background: var(--paper); }
  .blue-field {
    position: absolute; left: 0; right: 0; bottom: 0;
    background: linear-gradient(150deg, var(--cyan) 0%, var(--teal) 35%, var(--navy) 100%);
  }
  .card--front { left: 240px; top: 12px; width: 750px; height: 428px; }
  .card--front-small { left: 614px; top: 456px; width: 520px; height: 296px; }
  .card--front .blue-field, .card--front-small .blue-field { top: 0; }

  .card--back-small { left: 77px; top: 454px; width: 529px; height: 302px; }
  .card--back-small .blue-field { top: 144px; }
  .card--letter { left: 240px; top: 762px; width: 756px; height: 432px; }
  .card--letter .blue-field { top: 208px; }

  .brand { position: absolute; display: flex; align-items: center; }
  .brand-square { flex: none; border-radius: 4px; }
  .brand-name { line-height: 1; letter-spacing: 0.02em; text-transform: uppercase; }
  .brand-name span { display: block; }

  .brand--light .brand-square { background: var(--paper); }
  .brand--light .brand-name { color: var(--paper); }
  .brand--dark .brand-square { background: var(--mark-grey); }
  .brand--dark .brand-name { color: var(--ink); }

  .card--front .brand { left: 235px; top: 138px; }
  .card--front .brand-square { width: 96px; height: 96px; margin-right: 22px; }
  .card--front .brand-name span:first-child { font-size: 46px; }
  .card--front .brand-name span:last-child { font-size: 27px; margin-top: 6px; }

  .card--front-small .brand { left: 230px; top: 124px; }
  .card--front-small .brand-square { width: 68px; height: 68px; margin-right: 15px; }
  .card--front-small .brand-name span:first-child { font-size: 33px; }
  .card--front-small .brand-name span:last-child { font-size: 19px; margin-top: 4px; }

  .card--back-small .brand { left: 16px; top: 16px; }
  .card--back-small .brand-square { width: 52px; height: 52px; margin-right: 11px; }
  .card--back-small .brand-name span:first-child { font-size: 26px; }
  .card--back-small .brand-name span:last-child { font-size: 15px; margin-top: 3px; }

  .card--letter .brand { left: 24px; top: 24px; }
  .card--letter .brand-square { width: 72px; height: 72px; margin-right: 16px; }
  .card--letter .brand-name span:first-child { font-size: 36px; }
  .card--letter .brand-name span:last-child { font-size: 21px; margin-top: 4px; }

  .practitioner { position: absolute; text-align: right; color: var(--ink); }
  .practitioner-name { display: block; line-height: 1.1; letter-spacing: 0.02em; }
  .practitioner-role { display: block; font-family: "EB Garamond", serif; font-style: italic; font-weight: 500; color: var(--mark-grey); margin-top: 3px; }
  .card--back-small .practitioner { right: 22px; top: 20px; }
  .card--back-small .practitioner-name { font-size: 16px; }
  .card--back-small .practitioner-role { font-size: 11px; }
  .card--letter .practitioner { right: 28px; top: 30px; }
  .card--letter .practitioner-name { font-size: 22px; }
  .card--letter .practitioner-role { font-size: 14px; }

  .appointment {
    position: absolute; display: flex; align-items: flex-end; gap: 10px;
    font-family: "EB Garamond", serif; font-style: italic; font-weight: 500; color: var(--ink);
  }
  .appointment-title { font-weight: 700; text-transform: uppercase; color: var(--label); }
  .write-line { display: inline-block; border-bottom: 1px solid var(--rule); }
  .card--back-small .appointment { left: 18px; right: 22px; top: 100px; font-size: 11px; }
  .card--back-small .write-line--date { width: 130px; }
  .card--back-small .write-line--time { width: 90px; }
  .card--letter .appointment { left: 26px; right: 28px; top: 146px; font-size: 15px; gap: 14px; }
  .card--letter .write-line--date { width: 210px; }
  .card--letter .write-line--time { width: 140px; }

  .contact {
    position: absolute; font-family: "EB Garamond", serif; font-style: italic;
    text-align: right; line-height: 1.42;
  }
  .contact dt { display: inline; font-weight: 700; color: var(--label); text-transform: uppercase; }
  .contact dd { display: inline; font-weight: 500; color: var(--value); margin-left: 5px; }
  .contact div { white-space: nowrap; }

  .card--back-small .contact { right: 26px; top: 182px; font-size: 9.5px; }
  .card--letter .contact { right: 26px; top: 262px; font-size: 12px; }
</style>
</head>
<body>

  <section class="card card--front" aria-label="Business card front">
    <div class="blue-field"></div>
    <div class="brand brand--light">
      <div class="brand-square"></div>
      <div class="brand-name"><span>Clearview</span><span>Wellbeing</span></div>
    </div>
  </section>

  <section class="card card--back-small" aria-label="Business card back">
    <div class="blue-field"></div>
    <div class="brand brand--dark">
      <div class="brand-square"></div>
      <div class="brand-name"><span>Clearview</span><span>Wellbeing</span></div>
    </div>
    <p class="practitioner">
      <span class="practitioner-name">Margaret Hale</span>
      <span class="practitioner-role">Director / Clinical Psychologist</span>
    </p>
    <p class="appointment">
      <span class="appointment-title">Next appointment</span>
      <span>Date</span><span class="write-line write-line--date"></span>
      <span>Time</span><span class="write-line write-line--time"></span>
    </p>
    <dl class="contact">
      <div><dt>Address#</dt><dd>24 Harlow Street, ASHBURN 6031</dd></div>
      <div><dt>Phone#</dt><dd>(08) 9312 4861 or 0412558207</dd></div>
      <div><dt>Email#</dt><dd>mhale@cvw.net.au</dd></div>
      <div><dt>Web#</dt><dd>www.cvw.net.au</dd></div>
      <div><dt>ABN#</dt><dd>41 826 305 917</dd></div>
      <div><dt>ACN#</dt><dd>208774361</dd></div>
    </dl>
  </section>

  <section class="card card--front-small" aria-label="Business card front, small">
    <div class="blue-field"></div>
    <div class="brand brand--light">
      <div class="brand-square"></div>
      <div class="brand-name"><span>Clearview</span><span>Wellbeing</span></div>
    </div>
  </section>

  <section class="card card--letter" aria-label="Business card back, large">
    <div class="blue-field"></div>
    <div class="brand brand--dark">
      <div class="brand-square"></div>
      <div class="brand-name"><span>Clearview</span><span>Wellbeing</span></div>
    </div>
    <p class="practitioner">
      <span class="practitioner-name">Margaret Hale</span>
      <span class="practitioner-role">Director / Clinical Psychologist</span>
    </p>
    <p class="appointment">
      <span class="appointment-title">Next appointment</span>
      <span>Date</span><span class="write-line write-line--date"></span>
      <span>Time</span><span class="write-line write-line--time"></span>
    </p>
    <dl class="contact">
      <div><dt>Address#</dt><dd>24 Harlow Street, ASHBURN 6031</dd></div>
      <div><dt>Phone#</dt><dd>(08) 9312 4861 or 0412558207</dd></div>
      <div><dt>Email#</dt><dd>mhale@cvw.net.au</dd></div>
      <div><dt>Web#</dt><dd>www.cvw.net.au</dd></div>
      <div><dt>ABN#</dt><dd>41 826 305 917</dd></div>
      <div><dt>ACN#</dt><dd>208774361</dd></div>
    </dl>
  </section>

</body>
</html>
```